Branded Flyer Template Libraries Brightmoor Funding

Create one-page flyer templates for equipment finance industry to provide a fast turnaround that consistent on-brand for educational and promotional flyers that can be quickly customized with partners logos. These will become a standard toolkit for marketing for use in Adobe Illustrator and editable. customer facing are business owners considering equipment financing typically used for leave behind flyers, email, and handouts. vendor facing to equipment dealers, manufacturers and sales reps who refer customers to us, typically used at trade shows, co branded flyers, and email promotions.
Requesting 1-2 flyer templates with concepts for educational, and promotional.
Brand guide and current flyers in circulation are uploaded as reference.
Look and feel
Each slider illustrates characteristics of the customer's brand and the style your logo design should communicate.

```html
<!DOCTYPE html>
<html lang="en">
<head>
<meta charset="utf-8">
<title>Brightmoor Funding – Flyer Templates</title>
<link href="https://fonts.googleapis.com/css2?family=Work+Sans:wght@400;500;600;700&display=swap" rel="stylesheet">
<style>
:root{
  --green:#064d27;
  --teal:#84b1ae;
  --grey:#d4d4d4;
  --stone:#e8e6e4;
  --mist:#f2f2f2;
  --ink:#2a2a2a;
  --rule:#c9cfcc;
  --edge:#7d9a8b;
}
*{margin:0;padding:0;box-sizing:border-box}
html,body{width:1200px;height:2279px;overflow:hidden;background:#fff}
body{font-family:"Work Sans",Arial,sans-serif;color:var(--ink)}
.stage{position:absolute;left:0;top:0;width:1372px;height:2605px;transform:scale(.87464);transform-origin:0 0}
.flyer{position:absolute;left:287px;width:781px;height:1104px;background:#fff;overflow:hidden;box-shadow:-10px 12px 22px rgba(0,0,0,.22)}
.flyer--promo{top:103px}
.flyer--edu{top:1367px}
.abs{position:absolute}
.header-art{background:linear-gradient(160deg,var(--grey) 0%,var(--teal) 100%)}
.header-art--promo{left:200px;top:0;width:581px;height:215px;border-bottom-left-radius:100% 100%}
.header-art--edu{left:0;top:0;width:781px;height:300px;background:linear-gradient(180deg,var(--stone) 0%,var(--stone) 45%,var(--teal) 100%);border-bottom-left-radius:50% 28%;border-bottom-right-radius:50% 28%}
.hero-title{font-family:"Work Sans",Arial,sans-serif;font-weight:700;color:var(--green);font-size:46px;line-height:50px;letter-spacing:-.5px}
.about{background:var(--green);color:#fff;display:flex;align-items:center}
.about h2{font-weight:500;font-size:24px;letter-spacing:.5px;width:238px;padding-left:43px;flex:none}
.about p{font-size:11.5px;line-height:18.5px;white-space:nowrap}
.headline{color:var(--green);font-weight:600;font-size:24px;letter-spacing:.2px}
.rule{height:1px;background:var(--rule)}
.chev{width:9px;height:9px;border-right:1px solid var(--rule);border-bottom:1px solid var(--rule);transform:rotate(45deg)}
.item-title{font-weight:500;font-size:15px;color:var(--ink);letter-spacing:.3px}
.item-title .mark{color:var(--teal);margin-right:6px;font-weight:400}
.item-body{font-size:11.5px;line-height:18.5px;color:var(--ink);white-space:nowrap}
.tile{background:var(--stone);padding:17px 15px}
.tile .item-body{margin-top:6px}
.subline{color:var(--green);font-weight:500;font-size:26px;line-height:31px}
.cta{background:var(--green);color:#fff;display:flex;align-items:center;border-radius:8px 0 0 8px}
.cta h3{font-weight:600;font-size:26px;width:104px;padding-left:26px;flex:none}
.cta p{font-size:11.5px;line-height:18.5px;white-space:nowrap}
.footer{position:absolute;left:0;bottom:0;width:781px;display:flex}
.footer .contact{background:var(--green);width:424px;color:#fff;display:flex;flex-direction:column;justify-content:center;padding-left:40px;gap:5px}
.footer .contact li{list-style:none;display:flex;align-items:center;gap:14px;font-size:14px}
.footer .brand{flex:1;background:var(--mist);display:flex;align-items:center;justify-content:center}
.wordmark{display:flex;align-items:center;gap:10px;color:var(--green);font-weight:600;font-size:17px;letter-spacing:.6px;text-transform:uppercase}
.wordmark .dot{width:44px;height:44px;border-radius:50%;border:4px solid var(--green)}
.puzzle{display:flex;border:1px solid var(--edge);border-radius:10px;overflow:hidden}
.puzzle .piece{flex:1;padding:18px 18px}
.puzzle .piece + .piece{border-left:1px solid var(--edge)}
.puzzle .piece:nth-child(odd){background:var(--stone)}
.puzzle .piece:nth-child(even){background:#f1f0ef}
.puzzle .item-body{margin-top:14px}
.card{border:1px solid var(--edge);border-radius:0 12px 0 0;background:linear-gradient(180deg,#f6f5f4,var(--stone));padding:10px 14px}
.card .item-body{margin-top:4px}
</style>
</head>
<body>
<div class="stage">

  <!-- Promotional flyer -->
  <section class="flyer flyer--promo">
    <div class="abs header-art header-art--promo" role="img" aria-label="Decorative header band in grey and teal"></div>
    <h1 class="abs hero-title" style="left:43px;top:88px">You’re<br>Worth<br>More.</h1>

    <div class="abs about" style="left:37px;top:260px;width:704px;height:83px;border-radius:12px">
      <h2>ABOUT US</h2>
      <p>Lorem ipsum dolor sit amet, consectetuer adipiscing elit, sed diam<br>nonummy nibh euismod tincidunt ut laoreet dolore magna aliquam erat<br>Lorem ipsum dolor sit amet, consectetuer adipiscing elit, sed diam</p>
    </div>

    <h2 class="abs headline" style="left:36px;top:372px">HEADLINE</h2>
    <svg class="abs" style="left:0;top:0" width="781" height="600" aria-hidden="true">
      <path d="M37 411H245Q257 411 257 423V561Q257 573 269 573H490" fill="none" stroke="var(--green)" stroke-width="1.5"/>
      <path d="M273 411H500Q512 411 512 423V561Q512 573 524 573H741" fill="none" stroke="var(--green)" stroke-width="1.5"/>
    </svg>
    <div class="abs" style="left:37px;top:430px;width:205px">
      <div class="item-title"><span class="mark">+</span>TITLE</div>
      <p class="item-body" style="margin-top:12px">Lorem ipsum dolor sit amet,<br>consectetuer adipiscing elit, sed<br>diam nonummy nibh euismod<br>tincidunt ut laoreet dolore magna<br>aliquam erat</p>
    </div>
    <div class="abs" style="left:282px;top:430px;width:205px">
      <div class="item-title"><span class="mark">+</span>TITLE</div>
      <p class="item-body" style="margin-top:12px">Lorem ipsum dolor sit amet,<br>consectetuer adipiscing elit, sed<br>diam nonummy nibh euismod<br>tincidunt ut laoreet dolore magna<br>aliquam erat</p>
    </div>
    <div class="abs" style="left:536px;top:430px;width:205px">
      <div class="item-title"><span class="mark">+</span>TITLE</div>
      <p class="item-body" style="margin-top:12px">Lorem ipsum dolor sit amet,<br>consectetuer adipiscing elit, sed<br>diam nonummy nibh euismod<br>tincidunt ut laoreet dolore magna<br>aliquam erat</p>
    </div>

    <h2 class="abs headline" style="left:38px;top:596px">HEADLINE</h2>
    <div class="abs rule" style="left:180px;top:610px;width:552px"></div>
    <div class="abs chev" style="left:726px;top:604px"></div>

    <div class="abs tile" style="left:38px;top:642px;width:344px;height:105px">
      <div class="item-title">TITLE</div>
      <p class="item-body">Lorem ipsum dolor sit amet, consectetuer adipiscing<br>elit, sed diam nonummy nibh euismod tincidunt ut<br>laoreet dolore magna aliquam erat</p>
    </div>
    <div class="abs tile" style="left:397px;top:642px;width:344px;height:105px">
      <div class="item-title">TITLE</div>
      <p class="item-body">Lorem ipsum dolor sit amet, consectetuer adipiscing<br>elit, sed diam nonummy nibh euismod tincidunt ut<br>laoreet dolore magna aliquam erat</p>
    </div>
    <div class="abs tile" style="left:38px;top:760px;width:344px;height:105px">
      <div class="item-title">TITLE</div>
      <p class="item-body">Lorem ipsum dolor sit amet, consectetuer adipiscing<br>elit, sed diam nonummy nibh euismod tincidunt ut<br>laoreet dolore magna aliquam erat</p>
    </div>
    <div class="abs tile" style="left:397px;top:760px;width:344px;height:105px">
      <div class="item-title">TITLE</div>
      <p class="item-body">Lorem ipsum dolor sit amet, consectetuer adipiscing<br>elit, sed diam nonummy nibh euismod tincidunt ut<br>laoreet dolore magna aliquam erat</p>
    </div>

    <div class="abs" style="left:38px;top:896px;width:166px;height:2px;background:var(--green)"></div>
    <p class="abs subline" style="left:38px;top:905px">Lorem ipsum dolor<br>sit amet</p>
    <div class="abs cta" style="left:329px;top:899px;width:452px;height:72px">
      <h3>CTA</h3>
      <p>Lorem ipsum dolor sit amet, consectetuer adipiscing<br>elit, sed diam nonummy nibh euismod tincidunt ut</p>
    </div>

    <footer class="footer" style="height:107px">
      <ul class="contact">
        <li><svg width="16" height="16" viewBox="0 0 16 16" fill="none" stroke="#fff" stroke-width="1.2"><circle cx="8" cy="8" r="7"/><path d="M1 8h14M8 1c3 3 3 11 0 14M8 1c-3 3-3 11 0 14"/></svg>brightmoorfunding.com</li>
        <li><svg width="16" height="16" viewBox="0 0 16 16" fill="none" stroke="#fff" stroke-width="1.2"><rect x="1" y="3" width="14" height="10"/><path d="M1 3l7 6 7-6"/></svg>email@brightmoorfunding.com</li>
        <li><svg width="16" height="16" viewBox="0 0 16 16" fill="none" stroke="#fff" stroke-width="1.2"><path d="M2 12c0-3 3-4 6-4s6 1 6 4l-2 1-1-2H5l-1 2z"/><path d="M8 2v3M3 4l2 2M13 4l-2 2"/></svg>(800) 555-0148</li>
      </ul>
      <div class="brand"><div class="wordmark"><span class="dot"></span>Brightmoor Funding</div></div>
    </footer>
  </section>

  <!-- Educational flyer -->
  <section class="flyer flyer--edu">
    <div class="abs header-art header-art--edu" role="img" aria-label="Decorative header band in stone and teal"></div>
    <div class="abs" style="left:0;top:30px;width:781px;display:flex;justify-content:center"><div class="wordmark"><span class="dot"></span>Brightmoor Funding</div></div>
    <h1 class="abs hero-title" style="left:0;top:206px;width:781px;text-align:center">You’re<br>Worth<br>More.</h1>

    <div class="abs about" style="left:50px;top:373px;width:670px;height:84px;border-radius:22px 0 0 22px">
      <h2>ABOUT US</h2>
      <p>Lorem ipsum dolor sit amet, consectetuer adipiscing elit, sed diam<br>nonummy nibh euismod tincidunt ut laoreet dolore magna aliquam erat<br>Lorem ipsum dolor sit amet, consectetuer adipiscing elit, sed diam</p>
    </div>

    <h2 class="abs headline" style="left:48px;top:481px">HEADLINE</h2>
    <div class="abs rule" style="left:193px;top:495px;width:520px"></div>
    <div class="abs chev" style="left:707px;top:489px"></div>

    <div class="abs puzzle" style="left:48px;top:534px;width:672px;height:165px">
      <div class="piece"><div class="item-title">TITLE</div><p class="item-body">Lorem ipsum dolor sit amet,<br>consectetuer adipiscing elit,<br>sed diam nonummy nibh<br>euismod tincidunt ut laoreet<br>dolore magna aliquam erat</p></div>
      <div class="piece"><div class="item-title">TITLE</div><p class="item-body">Lorem ipsum dolor sit amet,<br>consectetuer adipiscing elit,<br>sed diam nonummy nibh<br>euismod tincidunt ut laoreet<br>dolore magna aliquam erat</p></div>
      <div class="piece"><div class="item-title">TITLE</div><p class="item-body">Lorem ipsum dolor sit amet,<br>consectetuer adipiscing elit,<br>sed diam nonummy nibh<br>euismod tincidunt ut laoreet<br>dolore magna aliquam erat</p></div>
    </div>

    <h2 class="abs headline" style="left:51px;top:722px">HEADLINE</h2>
    <div class="abs rule" style="left:193px;top:736px;width:520px"></div>
    <div class="abs chev" style="left:707px;top:730px"></div>

    <div class="abs card" style="left:50px;top:773px;width:325px;height:79px">
      <div class="item-title">TITLE</div>
      <p class="item-body">Lorem ipsum dolor sit amet, consectetuer adipiscing<br>elit, sed diam nonummy nibh euismod</p>
    </div>
    <div class="abs card" style="left:394px;top:773px;width:325px;height:79px">
      <div class="item-title">TITLE</div>
      <p class="item-body">Lorem ipsum dolor sit amet, consectetuer adipiscing<br>elit, sed diam nonummy nibh euismod</p>
    </div>
    <div class="abs card" style="left:50px;top:872px;width:325px;height:79px">
      <div class="item-title">TITLE</div>
      <p class="item-body">Lorem ipsum dolor sit amet, consectetuer adipiscing<br>elit, sed diam nonummy nibh euismod</p>
    </div>
    <div class="abs card" style="left:394px;top:872px;width:325px;height:79px">
      <div class="item-title">TITLE</div>
      <p class="item-body">Lorem ipsum dolor sit amet, consectetuer adipiscing<br>elit, sed diam nonummy nibh euismod</p>
    </div>

    <footer class="footer" style="height:119px">
      <ul class="contact" style="padding-left:50px;gap:8px">
        <li style="font-size:15px"><svg width="17" height="17" viewBox="0 0 16 16" fill="none" stroke="#fff" stroke-width="1.2"><circle cx="8" cy="8" r="7"/><path d="M1 8h14M8 1c3 3 3 11 0 14M8 1c-3 3-3 11 0 14"/></svg>brightmoorfunding.com</li>
        <li style="font-size:15px"><svg width="17" height="17" viewBox="0 0 16 16" fill="none" stroke="#fff" stroke-width="1.2"><rect x="1" y="3" width="14" height="10"/><path d="M1 3l7 6 7-6"/></svg>email@brightmoorfunding.com</li>
        <li style="font-size:15px"><svg width="17" height="17" viewBox="0 0 16 16" fill="none" stroke="#fff" stroke-width="1.2"><path d="M2 12c0-3 3-4 6-4s6 1 6 4l-2 1-1-2H5l-1 2z"/><path d="M8 2v3M3 4l2 2M13 4l-2 2"/></svg>(800) 555-0148</li>
      </ul>
      <div class="brand"><div class="wordmark"><span class="dot"></span>Brightmoor Funding</div></div>
    </footer>
  </section>

</div>
</body>
</html>
```